Stationery Refresh For Local Mortgage Broker

We want to modernise and standardise our stationery, including: letterhead, presentation folder, email signature and business card.

The new stationery should be a more modern and professional take on our existing colour scheme and brand. (We do not want a complete overhaul.) A folder of approved stock photos can be found here: https://filebox.example-share.net/f/7kQzR2mTn4vWx9Lp3Yb8-HsdJe5Uc1Ga/view

Our current website is: www.brindlecovefin.com.au but we will be updating this to be consistent with our new stationery.

We are open to *very slight* tweaks to our logo if you feel it needs modernising, but overall we would like to maintain consistent colour scheme.

> Letterhead

148 Calloway Parade,
Geelong, VIC, 3220
ABN: 31 805 249 067
Australian Credit License: 718293

(03) 5391 6084
www.brindlecovefin.com.au

> Presentation Folder

148 Calloway Parade,
Geelong, VIC, 3220
(03) 5391 6084
www.brindlecovefin.com.au

ABN: 31 805 249 067

> Email Signature

Liam Tresidder
Director
M. 0412 857 294
P. (03) 5391 6084
www.brindlecovefin.com.au
148 Calloway Parade,
Geelong, VIC, 3220

ABN: 31 805 249 067

(you can also include a photo if you like: https://brindlecovefin.com.au/wp-content/uploads/2020/12/Liam-Tresidder.png.webp)

> Business Card

Liam Tresidder
Director
M. 0412 857 294
P. (03) 5391 6084
www.brindlecovefin.com.au
148 Calloway Parade,
Geelong, VIC, 3220

ABN: 31 805 249 067

Additional information...

If it's useful/relevant, the services we offer are: Home Loans, Investment Loans, Refinance, Debt Consolidation, Commercial Finance, Vehicle Loans
(You may choose to use this in any of the designs)

Target Market(s)

Home Buyers and Investors

Industry/Entity Type

Mortgage broking/property/real estate

Requirements
Must have
• At least somewhat consistent with our current site (yet meaningfully modernized)
Should not have
• dramatically different logo or colourscheme overhauls

```html
<!DOCTYPE html>
<html lang="en">
<head>
<meta charset="utf-8">
<title>Brindle Cove Financial Services – Business Card</title>
<link rel="stylesheet" href="https://fonts.googleapis.com/css2?family=Roboto:wght@400;500;700&display=swap">
<style>
  :root {
    --brand-red: #b0141f;
    --brand-red-light: #c21e2b;
    --paper: #ffffff;
    --ink: #4a4a4a;
    --rule: #8a8a8a;
    --stage: #2a2a2c;
  }
  * { box-sizing: border-box; margin: 0; padding: 0; }
  html, body { width: 1200px; height: 929px; overflow: hidden; }
  body {
    background: var(--stage);
    font-family: "Roboto", Arial, sans-serif;
    position: relative;
  }
  .card {
    position: absolute;
    width: 560px;
    height: 320px;
    border-radius: 3px;
    box-shadow: 0 14px 30px rgba(0,0,0,.45);
    overflow: hidden;
  }
  /* Front */
  .card--front {
    left: 70px; top: 90px;
    background: linear-gradient(160deg, var(--brand-red) 0%, var(--brand-red-light) 100%);
    color: var(--paper);
    text-align: center;
  }
  .wordmark {
    font-weight: 400;
    text-transform: uppercase;
    line-height: 1.3;
  }
  .card--front .wordmark {
    margin-top: 92px;
  }
  .wordmark__name { display: block; font-size: 34px; letter-spacing: 10px; }
  .wordmark__tag { display: block; font-size: 13px; letter-spacing: 7px; }
  .services {
    margin-top: 40px;
    font-size: 12.5px;
    font-weight: 500;
    line-height: 1.8;
  }
  .services span { margin: 0 6px; }
  .services span::before { content: "●"; font-size: 8px; margin-right: 4px; vertical-align: 2px; }

  /* Back */
  .card--back {
    left: 570px; top: 500px;
    background: var(--paper);
  }
  .card--back .wordmark {
    position: absolute;
    left: 30px; top: 112px;
    width: 230px;
    color: var(--brand-red);
    text-align: center;
  }
  .card--back .wordmark__name { font-size: 20px; letter-spacing: 5px; }
  .card--back .wordmark__tag { font-size: 8px; letter-spacing: 4px; }
  .divider {
    position: absolute;
    left: 282px; top: 40px;
    width: 1px; height: 176px;
    background: var(--rule);
  }
  .contact {
    position: absolute;
    left: 302px; top: 36px;
    color: var(--ink);
    font-size: 13px;
    line-height: 1.35;
  }
  .contact__name { color: var(--brand-red); font-weight: 700; font-size: 16px; text-transform: uppercase; }
  .contact__role { margin-bottom: 10px; }
  .contact__address { margin-bottom: 8px; }
  .contact__list { list-style: none; }
  .contact__list li { display: flex; align-items: center; gap: 7px; height: 19px; }
  .contact__list svg { width: 12px; height: 12px; fill: var(--brand-red); flex: none; }
  .legal-band {
    position: absolute;
    left: 0; right: 0; bottom: 18px;
    height: 40px;
    background: var(--brand-red);
    color: var(--paper);
    font-size: 13px;
    display: flex; align-items: center; justify-content: center;
    letter-spacing: .3px;
  }
</style>
</head>
<body>

<section class="card card--front">
  <div class="wordmark">
    <span class="wordmark__name">Brindle Cove</span>
    <span class="wordmark__tag">Financial Services</span>
  </div>
  <div class="services">
    <div><span>Home Loans</span><span>Investment Loans</span><span>Refinance</span></div>
    <div><span>Debt Consolidation</span><span>Commercial Finance</span><span>Vehicle Loans</span></div>
  </div>
</section>

<section class="card card--back">
  <div class="wordmark">
    <span class="wordmark__name">Brindle Cove</span>
    <span class="wordmark__tag">Financial Services</span>
  </div>
  <div class="divider"></div>
  <div class="contact">
    <div class="contact__name">Liam Tresidder</div>
    <div class="contact__role">Director</div>
    <div class="contact__address">148 Calloway Parade,<br>Geelong, VIC, 3220</div>
    <ul class="contact__list">
      <li><svg viewBox="0 0 12 12"><path d="M3 0h6a1 1 0 0 1 1 1v10a1 1 0 0 1-1 1H3a1 1 0 0 1-1-1V1a1 1 0 0 1 1-1zm0 1.5v8h6v-8zM5 10.3h2v.8H5z"/></svg>0412 857 294</li>
      <li><svg viewBox="0 0 12 12"><path d="M1 3.5C1 2 3 1.5 6 1.5s5 .5 5 2v1.2H8.6V3.6H3.4v1.1H1zM3 5.5h6l2 5.5H1zm3 1.2a1.6 1.6 0 1 0 0 3.2 1.6 1.6 0 0 0 0-3.2z"/></svg>(03) 5391 6084</li>
      <li><svg viewBox="0 0 12 12"><path d="M0 2h12v8H0zm1 1v.3l5 3.4 5-3.4V3zm0 1.5V9h10V4.5L6 8z"/></svg>info@brindlecovefin.com.au</li>
      <li><svg viewBox="0 0 12 12"><circle cx="6" cy="6" r="6"/><path d="M3 3.5c1 0 1.5.8 2.2.6.6.4.2 1.3-.5 1.5-.6.6 0 1.5-.6 2.3C3.4 7.4 2.6 5 3 3.5zm4.3-.8c.9.3 2 1.2 2 2.4-.7-.3-1.4.2-2-.4-.2-.6.5-1.1 0-2z" fill="#fff"/></svg>www.brindlecovefin.com.au</li>
    </ul>
  </div>
  <div class="legal-band">ABN: 31 805 249 067 &nbsp;|&nbsp; Australian Credit License: 718293</div>
</section>

</body>
</html>
```